Business Card Design Project

Business card design with a funky, clean, modern design. Business is an immigration consultancy. Client base will be Canadian employers wanting to hire or retain foreign workers and foreign nationals wanting to immigrate to Canada.

Full color possible, but should incorporate red/white/black as per the logo to be provided. Double sided card design.

Target Market(s)

Canadian employers looking to hire/retain staff and also foreign nationals immigrating to Canada

Industry/Entity Type

Business

Requirements
Must have
• Logo (to be provided)
Name (Marla Voskuil, Immigration Consultant)
Phone (604) 731-5562
E-mail: marla@tallowbrookmigration.example
Web: www.tallowbrookmigration.example

Nice to have
• Tag Line
Clean, modern style

```html
<!DOCTYPE html>
<html lang="en">
<head>
<meta charset="utf-8">
<title>Tallowbrook Migration – Business Card</title>
<link rel="stylesheet" href="https://fonts.googleapis.com/css2?family=Open+Sans:wght@400;600&display=swap">
<style>
  :root {
    --bg: #d9d9d9;
    --card: #1c1b1c;
    --card-edge: #262526;
    --red: #c41a1f;
    --white: #f2f2f2;
    --grey: #bdbdbd;
    --faint: #2c2b2c;
  }
  * { margin: 0; padding: 0; box-sizing: border-box; }
  html, body {
    width: 1200px; height: 900px; overflow: hidden;
    background: var(--bg);
    font-family: "Open Sans", sans-serif;
  }
  .stage {
    width: 1200px; height: 900px;
    display: flex; flex-direction: column;
    align-items: center; justify-content: center; gap: 36px;
  }
  .card {
    position: relative;
    width: 700px; height: 400px;
    background: linear-gradient(135deg, var(--card-edge), var(--card));
    overflow: hidden;
    box-shadow: 0 10px 24px rgba(0,0,0,0.25);
  }
  .card svg.deco { position: absolute; inset: 0; }

  /* Back side */
  .back .brand {
    position: absolute; left: 410px; top: 120px; width: 260px;
    display: flex; flex-direction: column; align-items: center; gap: 10px;
  }
  .brand-mark {
    width: 34px; height: 34px; border-radius: 50%;
    background: var(--red);
  }
  .brand-name {
    color: var(--white); font-weight: 600; font-size: 24px;
    letter-spacing: 2px; text-transform: uppercase; text-align: center; line-height: 1.25;
  }
  .back .web {
    position: absolute; left: 410px; width: 260px; top: 300px;
    text-align: center; color: var(--grey); font-size: 13px;
  }

  /* Front side */
  .front .person { position: absolute; left: 36px; top: 190px; }
  .person-name { color: var(--white); font-size: 22px; font-weight: 400; }
  .person-title { color: var(--red); font-size: 14px; margin-top: 2px; }
  .contact { list-style: none; margin-top: 24px; }
  .contact li {
    display: flex; align-items: center; gap: 14px;
    color: var(--white); font-size: 14px; line-height: 27px;
  }
  .contact svg { width: 15px; height: 15px; flex: none; }
  .front .brand {
    position: absolute; left: 440px; top: 110px; width: 240px;
    display: flex; flex-direction: column; align-items: center; gap: 14px;
  }
  .front .brand-mark { width: 44px; height: 44px; }
  .front .brand-name { font-size: 24px; }
</style>
</head>
<body>
<main class="stage">

  <section class="card back" aria-label="Card back">
    <svg class="deco" width="700" height="400" aria-hidden="true">
      <circle cx="200" cy="260" r="170" fill="var(--faint)"/>
    </svg>
    <div class="brand">
      <span class="brand-mark"></span>
      <span class="brand-name">Tallowbrook<br>Migration</span>
    </div>
    <p class="web">www.tallowbrookmigration.example</p>
  </section>

  <section class="card front" aria-label="Card front">
    <svg class="deco" width="700" height="400" aria-hidden="true">
      <path d="M240 0 C345 75 388 240 360 400 L352 400 C378 240 336 80 232 0 Z" fill="var(--white)"/>
      <path d="M252 0 C362 72 406 240 380 400 L364 400 C392 240 350 76 244 0 Z" fill="var(--red)"/>
    </svg>
    <div class="person">
      <p class="person-name">Marla Voskuil</p>
      <p class="person-title">RCIC</p>
      <ul class="contact">
        <li>
          <svg viewBox="0 0 16 16"><rect x="3" y="1" width="10" height="14" rx="2" fill="var(--red)"/><rect x="5" y="3" width="6" height="7" fill="var(--card)"/></svg>
          (604) 731-5562
        </li>
        <li>
          <svg viewBox="0 0 16 16"><rect x="1" y="3" width="14" height="10" fill="none" stroke="var(--red)" stroke-width="1.6"/><path d="M1 3 L8 9 L15 3" fill="none" stroke="var(--red)" stroke-width="1.6"/></svg>
          marla@tallowbrookmigration.example
        </li>
        <li>
          <svg viewBox="0 0 16 16"><circle cx="8" cy="8" r="7" fill="var(--red)"/><path d="M1 8 H15 M8 1 V15" stroke="var(--card)" stroke-width="1.2"/></svg>
          www.tallowbrookmigration.example
        </li>
      </ul>
    </div>
    <div class="brand">
      <span class="brand-mark"></span>
      <span class="brand-name">Tallowbrook<br>Migration</span>
    </div>
  </section>

</main>
</body>
</html>
```